Flooring Billboard Highlighting Large In Stock Inventory

Looking to create a billboard that primarily highlights our logo but also calls out our large in stock inventory and has the city we are located in and phone number at the bottom. Looking for a professional looking design, that is simplistic yet informative.

Location: Tamarack, WI, Near Exit 142

Phone: (715) 638-4907

Website: www.plankharborwi.com

Products: Carpet, Hardwood, Laminate, Vinyl, Luxury Vinyl Plank & Window Treatments

Callouts:
-Free Estimates
-Wisconsin's In Stock Flooring Store
-Slogan: "Big city selection, small town service"

Target Market(s)

Home buyers, DIY'ers, Remoderls, designers

Industry/Entity Type

Flooring, Construction

Font styles to use
Serif

Requirements
Must have
• My logo, location, phone number and call out our large in stock inventory
Nice to have
• Call out the products we have and our slogan

```html
<!DOCTYPE html>
<html lang="en">
<head>
<meta charset="utf-8">
<title>Plank Harbor Billboard</title>
<link rel="stylesheet" href="https://fonts.googleapis.com/css2?family=Outfit:wght@300;400;500;700;800&family=Barlow+Semi+Condensed:wght@700&display=swap">
<style>
  :root {
    --orange: #bf6529;
    --teal: #138a86;
    --teal-deep: #0b5f5b;
    --ink: #2a2a2a;
    --strip: #f2f2f2;
    --white: #ffffff;
    --backdrop: #444444;
  }
  * { box-sizing: border-box; margin: 0; padding: 0; }
  html, body { width: 1059px; height: 1200px; overflow: hidden; background: var(--backdrop); }
  body { position: relative; font-family: "Outfit", sans-serif; }

  .billboard {
    position: absolute; left: 30px; top: 458px;
    width: 1000px; height: 283px; background: var(--white); overflow: hidden;
  }
  .headline-panel {
    position: absolute; left: 0; top: 0; width: 302px; height: 197px;
    background: var(--orange);
    clip-path: polygon(0 0, 263px 0, 302px 104px, 267px 197px, 0 197px);
  }
  .headline {
    position: absolute; left: 31px; top: 22px; color: var(--white);
    font-weight: 800; line-height: 0.98; text-transform: uppercase;
  }
  .headline .lead { display: block; font-size: 29px; letter-spacing: 0.2px; margin-bottom: 3px; }
  .headline .big { display: block; font-size: 45px; letter-spacing: -0.5px; }

  .brand {
    position: absolute; left: 302px; top: 0; width: 384px; height: 197px;
    display: flex; align-items: center; justify-content: center; gap: 12px;
  }
  .brand-mark { width: 34px; height: 34px; background: var(--teal); }
  .brand-name { font-size: 50px; font-weight: 500; color: var(--orange); letter-spacing: -0.5px; white-space: nowrap; }

  .slogan-panel {
    position: absolute; left: 686px; top: 0; width: 314px; height: 197px;
    clip-path: polygon(37px 0, 314px 0, 314px 197px, 34px 197px, 0 104px);
  }
  .slogan-backdrop {
    position: absolute; inset: 0;
    background: linear-gradient(135deg, var(--teal) 0%, var(--teal-deep) 100%);
  }
  .slogan {
    position: absolute; left: 0; right: 0; top: 20px; text-align: center; color: var(--white);
    padding-left: 30px;
  }
  .slogan .selection { display: block; font-size: 37px; font-weight: 300; line-height: 0.92; text-transform: uppercase; letter-spacing: -0.3px; }
  .slogan .service { display: block; font-size: 22px; font-weight: 800; margin-top: 2px; }
  .location {
    position: absolute; left: 82px; top: 131px; width: 176px; height: 66px;
    background: var(--orange); border-radius: 9px 9px 0 0; color: var(--white);
    font-size: 22px; font-weight: 300; line-height: 1.0; text-align: center;
    display: flex; flex-direction: column; justify-content: center;
  }

  .product-strip {
    position: absolute; left: 0; top: 197px; width: 1000px; height: 37px;
    background: var(--strip); display: flex; align-items: center; justify-content: space-between;
    padding: 0 30px; list-style: none;
  }
  .product-strip li {
    font-size: 16.5px; font-weight: 500; color: var(--ink); text-transform: uppercase; white-space: nowrap;
    display: flex; align-items: center; gap: 11px;
  }
  .product-strip li::before {
    content: ""; width: 6px; height: 6px; border-radius: 50%; background: var(--orange);
  }

  .contact-bar {
    position: absolute; left: 0; top: 234px; width: 1000px; height: 49px;
    background: var(--ink); display: flex; align-items: center; padding: 0 22px; color: var(--white);
  }
  .estimates {
    font-family: "Barlow Semi Condensed", sans-serif; font-weight: 700; font-size: 30px;
    color: var(--orange); text-transform: uppercase; letter-spacing: 0.2px;
  }
  .contact-icon { width: 22px; height: 28px; margin-left: 22px; margin-right: 12px; flex: none; }
  .phone { font-size: 35px; font-weight: 500; letter-spacing: 0.3px; }
  .globe { width: 24px; height: 24px; margin-left: 22px; margin-right: 18px; }
  .website { font-size: 32px; font-weight: 500; letter-spacing: 0.2px; }
</style>
</head>
<body>
  <section class="billboard">
    <div class="headline-panel">
      <h1 class="headline">
        <span class="lead">Wisconsin's</span>
        <span class="big">In Stock</span>
        <span class="big">Flooring</span>
        <span class="big">Store</span>
      </h1>
    </div>

    <div class="brand">
      <span class="brand-mark"></span>
      <span class="brand-name">Plank Harbor</span>
    </div>

    <div class="slogan-panel">
      <div class="slogan-backdrop" role="img" aria-label="Teal-toned photo of a modern living room interior"></div>
      <p class="slogan">
        <span class="selection">Big City<br>Selection,</span>
        <span class="service">Small town service</span>
      </p>
      <p class="location">Tamarack, WI,<br>Near Exit 142</p>
    </div>

    <ul class="product-strip">
      <li>Carpet</li>
      <li>Hardwood</li>
      <li>Laminate</li>
      <li>Vinyl</li>
      <li>Luxury Vinyl Plank &amp;</li>
      <li>Window Treatments</li>
    </ul>

    <div class="contact-bar">
      <span class="estimates">Free Estimates</span>
      <svg class="contact-icon" viewBox="0 0 20 24" aria-hidden="true">
        <path d="M7 2 L10 2 L10 7 L7.5 8.5 C7 12 8 15.5 10 18 L12.5 16.5 L15 20.5 L12 22.5 C7 22 3.5 15 4 8 C4.3 5 5.5 3 7 2 Z" fill="var(--orange)"/>
      </svg>
      <span class="phone">(715) 638-4907</span>
      <svg class="contact-icon globe" viewBox="0 0 24 24" aria-hidden="true">
        <g fill="none" stroke="var(--orange)" stroke-width="2">
          <circle cx="12" cy="12" r="10"/>
          <ellipse cx="12" cy="12" rx="4.5" ry="10"/>
          <line x1="2" y1="12" x2="22" y2="12"/>
          <line x1="4" y1="6.5" x2="20" y2="6.5"/>
          <line x1="4" y1="17.5" x2="20" y2="17.5"/>
        </g>
      </svg>
      <span class="website">plankharborwi.com</span>
    </div>
  </section>
</body>
</html>
```